The Fern Barrel Pub- restaurant menu, new launch

This is a new restaurant launching Summer 2017. Restaurant is a conversion of long standing small town existing family pizza/italian restaurant. new concept shifts concept to a family pub atmosphere featuring familiar appetizers, burgers, wood-fired pizza, and daily specials, draft beer, full- bar.

atmosphere is casual. want menu to reflect a more current "vibe" than the old place did. Not cold and modern, but retain the cozy familiar feel, without seeming dated and old fashioned.

4 panel menu; 8.5 X 11; 2-4 color
Updates

Project Deadline Extended
Reason: I am interested in seeing more designs. I will be providing feedback in the next few days on all designs submitted. I will also be increasing the budget.

Target Market(s)

Family-Oriented Pub, rural location Berkshire County, MA. Mostly Blue collar customer, value oriented

Industry/Entity Type

American Restaurant

Font styles to use
Sans Serif

Colors

Designer to choose colors to be used in the design.

Requirements
Must have
• Clear, uncluttered design, Highlighted items as specified in draft file (to come)
• ability to make changes daily as menu changes
• each panel separate sheet to slide into binder sleeve

```html
<!DOCTYPE html>
<html lang="en">
<head>
<meta charset="utf-8">
<title>Daily Specials – The Fern Barrel Pub</title>
<link rel="stylesheet" href="https://fonts.googleapis.com/css2?family=Alike&family=Delius&family=Julius+Sans+One&display=swap">
<style>
  :root {
    --paper: #f6efe8;
    --ink: #4a4443;
    --accent: #e3231f;
    --sketch: #e9e0d6;
  }
  * { margin: 0; padding: 0; box-sizing: border-box; }
  html, body { width: 927px; height: 1200px; overflow: hidden; background: var(--paper); }
  .menu-sheet {
    position: relative;
    width: 927px;
    height: 1200px;
    background: var(--paper);
    color: var(--ink);
    overflow: hidden;
  }
  .produce-sketch {
    position: absolute;
    left: 0;
    bottom: 0;
    width: 927px;
    height: 300px;
    z-index: 0;
  }
  .sheet-title {
    position: absolute;
    top: 52px;
    left: 0;
    width: 100%;
    text-align: center;
    font-family: "Alike", serif;
    font-weight: 400;
    font-size: 57px;
    line-height: 60px;
    letter-spacing: -0.5px;
    z-index: 1;
  }
  .tagline-band {
    position: absolute;
    top: 110px;
    left: 218px;
    width: 468px;
    height: 49px;
    background: var(--accent);
    color: #fff;
    font-family: "Julius Sans One", sans-serif;
    font-size: 26px;
    line-height: 49px;
    text-align: center;
    letter-spacing: 0.5px;
    z-index: 1;
  }
  .column-divider {
    position: absolute;
    top: 194px;
    left: 457px;
    width: 2px;
    height: 708px;
    background: var(--accent);
    z-index: 1;
  }
  .special {
    position: absolute;
    text-align: center;
    z-index: 1;
  }
  .special-name {
    font-family: "Alike", serif;
    font-weight: 400;
    font-size: 39px;
    line-height: 45px;
    color: var(--ink);
    padding-bottom: 8px;
    border-bottom: 3px solid var(--ink);
    white-space: nowrap;
  }
  .special-name .cents { font-size: 32px; }
  .special-desc {
    font-family: "Delius", sans-serif;
    font-size: 17px;
    line-height: 25.5px;
    color: var(--accent);
    margin-top: 12px;
    white-space: nowrap;
  }
  .lasagna    { top: 199px; left: 84px;  width: 333px; }
  .pig-pile   { top: 413px; left: 99px;  width: 307px; }
  .carbonara  { top: 677px; left: 101px; width: 307px; }
  .primavera  { top: 206px; left: 494px; width: 332px; }
  .parmesan   { top: 418px; left: 494px; width: 332px; }
  .buffalo    { top: 686px; left: 522px; width: 334px; }
  .pig-pile .special-desc,
  .parmesan .special-desc { margin-top: 13px; }
</style>
</head>
<body>
<main class="menu-sheet">
  <svg class="produce-sketch" role="img" aria-label="Hand-drawn line sketch of a bell pepper, bow-tie pasta, a tomato, herbs, mushrooms and a wooden board along the bottom edge" viewBox="0 0 927 300" preserveAspectRatio="none">
    <defs>
      <linearGradient id="sketchTone" x1="0" y1="0" x2="0" y2="1">
        <stop offset="0" stop-color="#f6efe8"/>
        <stop offset="1" stop-color="#e9e0d6"/>
      </linearGradient>
    </defs>
    <rect width="927" height="300" fill="url(#sketchTone)"/>
  </svg>

  <h1 class="sheet-title">DAILY SPECIALS</h1>
  <div class="tagline-band">WHERE THE CRAZINESS BEGINS</div>
  <div class="column-divider"></div>

  <section class="special lasagna">
    <h2 class="special-name">20 Layer<br>Lasagna&nbsp; <span class="price">$12.<span class="cents">99</span></span></h2>
    <p class="special-desc">Our signature dish. Sells out every week,<br>get it when you can</p>
  </section>

  <section class="special pig-pile">
    <h2 class="special-name">The Pig Pile&nbsp; <span class="price">$11</span></h2>
    <p class="special-desc">Our World-class Hand-cut fries<br>topped with Pulled pork, Mozzarella,<br>Crispy Bacon, BBQ sauce and Topped<br>with house onion rings. Not for<br>the faint of heart, if you<br>know what we mean...</p>
  </section>

  <section class="special carbonara">
    <h2 class="special-name">Pasta Carbonara<br><span class="price">$15</span></h2>
    <p class="special-desc">The creamy bacon pasta classic.<br>You know it, you love it.&nbsp; Just say yes.</p>
  </section>

  <section class="special primavera">
    <h2 class="special-name">Pasta Primavera<br><span class="price">$12.<span class="cents">99</span></span></h2>
    <p class="special-desc">Fresh veggies, tossed with penne,<br>in a garlic white wine butter sauce</p>
  </section>

  <section class="special parmesan">
    <h2 class="special-name">Chicken Parmesan<br><span class="price">$15</span></h2>
    <p class="special-desc">Two breaded chicken breasts topped<br>with house marinara and mozzarella,<br>served with penne marinara.&nbsp; Yum.<br>Fresh veggies, tossed with penne,<br>in a garlic white wine butter sauce</p>
  </section>

  <section class="special buffalo">
    <h2 class="special-name">Buffalo Chicken<br>Mac &amp; Cheese&nbsp; <span class="price">$13</span></h2>
    <p class="special-desc">All the food groups in this one!<br>Chicken, Buffalo sauce, Mac and Cheese.<br>A true food pyramid!</p>
  </section>
</main>
</body>
</html>
```